依頼詳細
シニア向け通販媒体にて展開するA5サイズ片面カラーのチラシの作成を依頼致します。年配者の女性をターゲットにしていますので、読みやすく、安心感がありかつ雰囲気のあるデザインを期待致します。
記載項目
詳しくは添付の指示書、画像をご確認をお願い申し上げます。
サイズ
A5
ページ数
片面
希望イメージ
• +5 0 +5
• シンプル
複雑
• 単色
カラフル
• 暗い
明るい
• 日常
高級
• 遊び心
厳粛
• 未来的
伝統的
• 女性的
男性的
希望する色
赤系、黄・オレンジ系
納品ファイル
• イラストレーター形式 (.ai)
補足説明
依頼公開後の追記内容
申込書は別紙になりますので、会社名や申し込み方法や電話番号の記載は必要ございません。
パッケージ画像は1袋のみの掲載でお願い申し上げます。
■ 選んだ理由

インパクトがあり雰囲気もよく何より干しいもが美味しそうに見えるので採用させていただきました。

■ 提案者全員のお礼・コメント

皆様、たくさんの素晴らしいご提案をありがとうございます。
どのデザインも素晴らしくとても悩みました。
また機会がございましたらよろしくお願いいたします。

```html
<!DOCTYPE html>
<html lang="ja">
<head>
<meta charset="utf-8">
<title>ほっこり干しいも 雅</title>
<link rel="stylesheet" href="https://fonts.googleapis.com/css2?family=Noto+Sans+JP:wght@400;500;700;900&family=Shippori+Mincho:wght@500;700;800&family=Yuji+Syuku&display=swap">
<style>
  :root {
    --paper: #fbf4ec;
    --cream: #f6ebdf;
    --red: #c8161d;
    --ink: #1d1a18;
    --brown: #4a3226;
    --green: #3aa35a;
    --blue: #2b8fcf;
    --gold: #f5b800;
    --potato: #f2a43a;
    --potato-light: #fbd58a;
    --plate: #e9e4de;
    --panel: #fdeeea;
    --white: #ffffff;
  }
  * { margin: 0; padding: 0; box-sizing: border-box; }
  html, body { width: 844px; height: 1200px; overflow: hidden; background: var(--paper); }
  .flyer {
    position: relative; width: 844px; height: 1200px; overflow: hidden;
    background: linear-gradient(180deg, var(--paper) 0%, var(--cream) 100%);
    font-family: "Noto Sans JP", sans-serif; color: var(--ink);
  }
  .photo { position: absolute; }
  .photo-potatoes {
    left: 0; top: 0; width: 320px; height: 260px;
    background: radial-gradient(ellipse at 45% 45%, #8c3a4e 0%, #6b2a3a 45%, #c9a57a 80%, var(--paper) 100%);
    border-bottom-right-radius: 60px;
  }
  .photo-plate {
    left: 0; top: 200px; width: 844px; height: 740px;
    background: radial-gradient(ellipse at 40% 45%, var(--potato-light) 0%, var(--potato) 30%, #e68a2a 42%, var(--plate) 52%, #d9d2ca 64%, var(--paper) 74%);
  }
  .origin-label {
    position: absolute; left: 18px; top: 262px; width: 46px; padding: 12px 0;
    background: var(--red); color: var(--white);
    writing-mode: vertical-rl; text-orientation: upright;
    font-family: "Shippori Mincho", serif; font-weight: 700; font-size: 22px; letter-spacing: 2px;
    display: flex; align-items: center;
  }
  .origin-label .variety { color: #ffe27a; }
  .badge-zeppin { position: absolute; left: 604px; top: 76px; display: flex; }
  .badge-zeppin span {
    width: 82px; height: 82px; display: flex; align-items: center; justify-content: center;
    font-family: "Shippori Mincho", serif; font-weight: 800; font-size: 58px;
  }
  .badge-zeppin .filled { background: var(--red); color: var(--white); }
  .badge-zeppin .outlined { background: var(--white); color: var(--red); border: 3px solid var(--red); }
  .tagline {
    position: absolute; left: 610px; top: 196px;
    writing-mode: vertical-rl; font-family: "Shippori Mincho", serif; font-weight: 700;
    font-size: 30px; letter-spacing: 4px; color: var(--ink);
  }
  .headline {
    position: absolute; left: 684px; top: 190px;
    writing-mode: vertical-rl; font-family: "Yuji Syuku", serif; font-weight: 400;
    font-size: 122px; line-height: 1; color: var(--ink);
  }
  .story {
    position: absolute; left: 26px; top: 748px; width: 400px;
    font-family: "Shippori Mincho", serif; font-weight: 500; font-size: 16px; line-height: 1.75;
    color: var(--ink); background: rgba(255,255,255,0.6); padding: 8px 10px;
  }
  .seal {
    position: absolute; top: 704px; width: 132px; height: 132px; border-radius: 50%;
    display: flex; flex-direction: column; align-items: center; justify-content: center;
    color: var(--white); font-weight: 900; text-align: center; line-height: 1.2;
  }
  .seal-additive { left: 458px; background: var(--green); font-size: 24px; }
  .seal-volume { left: 598px; background: var(--blue); font-size: 20px; }
  .seal-volume strong { font-size: 40px; line-height: 1.05; }
  .seal-volume strong small { font-size: 26px; }
  .offer {
    position: absolute; left: 14px; top: 956px; width: 816px; height: 226px;
    background: var(--panel); border: 3px solid var(--red);
  }
  .photo-package {
    left: 26px; top: 10px; width: 240px; height: 200px; border-radius: 6px;
    background: linear-gradient(160deg, #f4ecec 0%, #e3a6a8 45%, #f0b054 75%, #f4ecec 100%);
  }
  .product-title {
    position: absolute; left: 290px; top: 18px; display: flex; align-items: center; gap: 14px;
    font-family: "Shippori Mincho", serif; font-weight: 700; font-size: 32px; color: var(--brown);
  }
  .product-title .grade { font-size: 52px; font-weight: 800; color: var(--ink); }
  .product-title .weight {
    font-family: "Noto Sans JP", sans-serif; font-size: 22px; font-weight: 900;
    background: var(--red); color: var(--white); padding: 2px 12px; margin-left: 36px;
  }
  .prices { position: absolute; left: 290px; top: 90px; width: 510px; border-collapse: collapse; }
  .prices td { padding: 3px 6px; font-size: 16px; font-weight: 700; white-space: nowrap; }
  .prices .plan { background: var(--red); color: var(--white); text-align: center; width: 170px; }
  .prices .plan-set { background: var(--gold); color: var(--ink); }
  .prices .label { font-size: 13px; font-weight: 500; width: 70px; }
  .prices .amount { color: var(--red); font-size: 24px; font-weight: 900; }
  .prices .amount small { font-size: 13px; color: var(--ink); font-weight: 500; }
  .prices tr + tr td { border-top: 6px solid transparent; }
  .notes { position: absolute; left: 292px; top: 192px; display: flex; gap: 28px; font-size: 13px; color: var(--brown); }
</style>
</head>
<body>
<main class="flyer">
  <div class="photo photo-plate" role="img" aria-label="白い皿に盛られた黄金色のやわらかい干しいも"></div>
  <div class="photo photo-potatoes" role="img" aria-label="かごに入った赤紫色のさつまいも"></div>

  <p class="origin-label">茨城県産<span class="variety">「紅はるか」</span>使用</p>

  <div class="badge-zeppin"><span class="filled">絶</span><span class="outlined">品</span></div>
  <p class="tagline">驚きの甘さとやわらかさ</p>
  <h1 class="headline">干しいも</h1>

  <p class="story">「紅はるか」は蜜芋とよばれるほど糖度が高く、柔らかい食感が特徴です。もう他の干しいもは食べられなくなるほど美味しい「ほっこり干しいも雅」を是非この機会にお試しください！</p>

  <div class="seal seal-additive">無添加<br>・<br>無着色</div>
  <div class="seal seal-volume">たっぷり<strong>200<small>g</small></strong></div>

  <section class="offer">
    <div class="photo photo-package" role="img" aria-label="干しいもの商品パッケージ 1袋"></div>
    <h2 class="product-title">ほっこり干しいも <span class="grade">雅</span><span class="weight">200g</span></h2>
    <table class="prices">
      <tr>
        <td class="plan">1 袋</td>
        <td class="label">本体価格</td>
        <td class="amount">978円<small>（税込1,056円）</small></td>
      </tr>
      <tr>
        <td class="plan plan-set">お買い得2袋セット</td>
        <td class="label">本体価格</td>
        <td class="amount">1,856円<small>（税込2,004円）</small></td>
      </tr>
    </table>
    <div class="notes"><span>●原材料/さつまいも（茨城県産）</span><span>●賞味期限/45日</span></div>
  </section>
</main>
</body>
</html>
```